Förderverein einer Kirchengemeinde sucht Flyer-Design
Zielgruppe
Wir sind ein Förderverein einer Kirchengemeinde, der sich für die kirchenmusikalische Arbeit einsetzt.
Wir wünschen uns ein niveauvolles und zeitgemäßes/modernes Flyerdesign, das die etablierten Konzertbesucher anspricht, aber vor allem auch Menschen erreicht und überzeugt, die (noch) nichts mit Kirche zu tun haben.
Das Alter der (Haupt-) Zielgruppe (Männer und Frauen) erstreckt sich von 45 bis 70 Jahren.
Aufgabenstellung
Bei der Wahl des Formates würden wir (aus der Sicht von Laien) ein zweimal gefaltetes DIN A4 quer Format nehmen. Aber wir lassen uns gerne überraschen und sind grundsätzlich für andere Lösungen offen.
Bitte den Abschnitt für Adress- und sonstige Dateneintragungen samt Kontodaten so gestalten und platzieren, dass man ihn leicht abtrennen und verschicken kann.
Der Flyer soll Kirchenmusik als lebendig und attraktiv darstellen und neue (jüngere) Mitglieder für den Freundeskreis werben.
Lassen Sie die Bilder sprechen!!

```html
<!DOCTYPE html>
<html lang="de">
<head>
<meta charset="utf-8">
<title>Freundeskreis Kirchenmusik – Flyer</title>
<link href="https://fonts.googleapis.com/css2?family=Noto+Serif:wght@400;700&family=PT+Sans:wght@400;700&display=swap" rel="stylesheet">
<style>
  :root{
    --red:#b5121b;
    --ink:#2a2a2a;
    --muted:#555;
    --rule:#7a7a7a;
    --paper:#ffffff;
    --page:#eceae8;
  }
  *{box-sizing:border-box;margin:0;padding:0}
  html,body{width:825px;height:1200px;overflow:hidden;background:var(--page)}
  body{position:relative;font-family:"PT Sans",Arial,sans-serif;color:var(--ink)}
  .spread{position:absolute;left:52px;width:720px;background:var(--paper);box-shadow:0 2px 8px rgba(0,0,0,.18)}
  .spread--outside{top:40px;height:517px}
  .spread--inside{top:625px;height:529px}
  .spread svg.art{position:absolute;left:0;top:0;width:720px;height:100%}
  .fold{position:absolute;top:0;bottom:0;width:1px;background:rgba(0,0,0,.08)}
  .block{position:absolute;font-size:9.5px;line-height:1.35}
  .block--small{font-size:8.5px;line-height:11px;width:200px}
  .heading{font-family:"Noto Serif",Georgia,serif;font-weight:700;color:var(--red);font-size:13.5px;line-height:1.2}
  .block p{margin-bottom:9px}
  .red{color:var(--red)}
  .field{position:absolute;border-top:1px solid var(--rule);font-size:6.5px;color:var(--muted);padding-top:2px}
  .brand{position:absolute;left:500px;top:402px;font-family:"Noto Serif",Georgia,serif;font-weight:400;font-size:31px;line-height:1.05;color:var(--red)}
  .reasons{list-style:none}
  .reasons li{position:relative;padding-left:14px;margin-bottom:10px}
  .reasons li::before{content:"";position:absolute;left:0;top:5px;width:4px;height:4px;border-radius:50%;background:var(--red)}
  .fees{list-style:none}
  .fees li{position:relative;padding-left:18px;margin-bottom:7px;font-size:9.5px}
  .fees li::before{content:"";position:absolute;left:0;top:1px;width:9px;height:9px;border:1.3px solid var(--red);border-radius:50%}
  .fees .blank{display:inline-block;width:108px;border-bottom:1px solid var(--rule);vertical-align:bottom}
  .fees small{display:block;font-size:5.5px;color:var(--muted)}
</style>
</head>
<body>

<section class="spread spread--outside">
  <svg class="art" viewBox="0 0 720 517" preserveAspectRatio="none">
    <defs>
      <linearGradient id="g-choir" x1="0" y1="0" x2="0" y2="1"><stop offset="0" stop-color="#c9b79a"/><stop offset="1" stop-color="#2c2a2a"/></linearGradient>
      <linearGradient id="g-organ" x1="0" y1="0" x2="1" y2="1"><stop offset="0" stop-color="#d9b98a"/><stop offset="1" stop-color="#5a3a22"/></linearGradient>
      <linearGradient id="g-brass" x1="0" y1="0" x2="1" y2="1"><stop offset="0" stop-color="#b8a47a"/><stop offset=".5" stop-color="#d7bf7c"/><stop offset="1" stop-color="#4a5360"/></linearGradient>
    </defs>
    <g role="img" aria-label="Foto: Chor und Orchester in der Kirche"><polygon points="0,354 240,443 240,517 0,517" fill="url(#g-choir)"/></g>
    <g role="img" aria-label="Foto: Orgelregister"><polygon points="240,0 480,0 480,38 240,112" fill="url(#g-organ)"/></g>
    <g role="img" aria-label="Foto: Blechbläser mit Trompete"><polygon points="480,12 720,44 720,242 480,100" fill="url(#g-brass)"/></g>
    <polygon points="0,340 483,511 483,517 0,347" fill="var(--red)"/>
    <polygon points="240,112 480,38 480,44 240,118" fill="var(--red)"/>
    <polygon points="480,0 720,32 720,40 480,8" fill="var(--red)"/>
    <polygon points="480,100 720,242 720,250 480,107" fill="var(--red)"/>
  </svg>
  <div class="fold" style="left:240px"></div>
  <div class="fold" style="left:480px"></div>

  <div class="block heading" style="left:24px;top:56px">SEPA-Lastschriftmandat</div>
  <div class="field" style="left:24px;top:103px;width:195px">BIC</div>
  <div class="field" style="left:24px;top:143px;width:195px">Kreditinstitut</div>
  <div class="field" style="left:24px;top:183px;width:195px">Kontoinhaber</div>
  <div class="block" style="left:24px;top:218px;width:200px">Hiermit ermächtige ich den Freundeskreis Kirchenmusik den von mir zu entrichtenden Mitgliedsbeitrag von meinem Konto einzuziehen.</div>
  <div class="field" style="left:24px;top:293px;width:62px">Ort, Datum</div>
  <div class="field" style="left:92px;top:293px;width:127px">Unterschrift</div>
  <div class="block" style="left:24px;top:318px;width:200px;text-align:right">Der Einzug der Mitgliedsbeiträge erfolgt zu Beginn eines Kalenderjahres.</div>

  <div class="block heading" style="left:264px;top:136px">Spendenkonto</div>
  <div class="block block--small" style="left:264px;top:160px">Kreissparkasse Heidmoor-Lindenau<br>IBAN: &nbsp;DE00123456780000000000<br>BIC: &nbsp;&nbsp;&nbsp;XXXXDE00HDM</div>
  <div class="block block--small" style="left:264px;top:198px">Verwendungszweck bei Einzelspenden<br>unter Angabe der Kostenstelle.</div>
  <div class="block heading" style="left:264px;top:240px">Kontakt</div>
  <div class="block block--small" style="left:264px;top:262px">Beitrittserklärungen bitte im Gemeindebüro<br>abgeben oder senden an:</div>
  <div class="block block--small" style="left:264px;top:290px">Freundeskreis Kirchenmusik<br>Geschäftsstelle:<br>Kirchengemeinde St. Lamberti,<br>Kirchgasse 7, 30000 Heidmoor</div>
  <div class="block block--small" style="left:264px;top:340px">Tel.: 01234-567890<br>info@freundeskreis-heidmoor.de</div>
  <div class="block block--small" style="left:264px;top:374px">Nähere Informationen zur Kirchenmusik<br>an St. Lamberti und zum Freundeskreis<br>finden Sie unter<br><span class="red">www.lamberti-heidmoor.de/musik</span></div>

  <div class="brand">Freundeskreis<br>Kirchenmusik</div>
</section>

<section class="spread spread--inside">
  <svg class="art" viewBox="0 0 720 529" preserveAspectRatio="none">
    <defs>
      <linearGradient id="g-group" x1="0" y1="0" x2="0" y2="1"><stop offset="0" stop-color="#c7c4bd"/><stop offset="1" stop-color="#4b4a4a"/></linearGradient>
      <linearGradient id="g-kids" x1="0" y1="0" x2="0" y2="1"><stop offset="0" stop-color="#3f6a33"/><stop offset=".55" stop-color="#e6d23a"/><stop offset="1" stop-color="#8a8a7a"/></linearGradient>
    </defs>
    <polygon points="0,6 480,0 480,8 0,14" fill="var(--red)"/>
    <g role="img" aria-label="Foto: Posaunenchor vor einem Gebäude"><polygon points="0,24 240,22 240,134 0,174" fill="url(#g-group)"/></g>
    <g role="img" aria-label="Foto: Kinderchor in gelben T-Shirts"><polygon points="240,22 480,18 480,86 240,134" fill="url(#g-kids)"/></g>
    <polygon points="0,174 480,86 480,93 0,181" fill="var(--red)"/>
  </svg>
  <div class="fold" style="left:240px"></div>
  <div class="fold" style="left:480px"></div>

  <div class="block" style="left:24px;top:190px;width:205px">
    <div class="heading" style="margin-bottom:26px">Gute Gründe für<br>eine Mitgliedschaft</div>
    <p style="margin-bottom:10px">Mitglieder</p>
    <ul class="reasons">
      <li>erhalten Eintrittskarten von gemeinde­eigenen Konzerten zu ermäßigten Preisen</li>
      <li>können Konzertkarten vor dem öffentlichen Verkauf erwerben</li>
      <li>gestalten die Arbeit des Freundeskreises in den jährlichen Mitgliederversammlungen aktiv mit</li>
      <li>erhalten aktuelle Informationen über Veranstaltungen der Gemeinde bequem per Email und profitieren so zu allererst</li>
      <li>können den Mitgliedsbeitrag steuerlich absetzen und erhalten eine Spenden­bescheinigung</li>
      <li>können an Ausflügen des Freundeskreises teilnehmen</li>
    </ul>
  </div>

  <div class="block" style="left:264px;top:136px;width:205px">
    <div class="heading" style="margin-bottom:10px">Kirchenmusik<br>braucht Freunde...</div>
    <p>Der Freundeskreis Kirchenmusik an St. Lamberti in Heidmoor wurde 1999 zur Förderung der Kirchenmusik gegründet.</p>
    <p>Die Mitglieder unterstützen mit ihren Beiträgen und Spenden die vielfältigen musikalischen Aktivitäten an der St. Lamberti-Kirche.</p>
    <p>Durch Ihren Beitritt bzw. Ihre Spende fördern Sie:</p>
    <ul class="reasons red" style="margin-bottom:8px">
      <li>Die Arbeit der Kantorei, des Posaunenchores, des Kinderchores und des Flötenensembles</li>
      <li>Die Pflege und Wartung der historischen Johann Brenner Orgel von 1748</li>
      <li>Den Erhalt, Pflege und ggf. Neuanschaffung der übrigen Instrumente</li>
      <li>Die Ausbildung des kirchenmusikalischen Nachwuchses</li>
      <li>Probenwochenende der Chöre</li>
    </ul>
    <p>Wir laden Sie ein, Mitglied in unserem Freundeskreis Kirchenmusik zu werden, um das kirchenmusikalische Niveau weiterhin zu halten und auch ausbauen zu können.</p>
  </div>

  <div class="block heading" style="left:504px;top:34px">Beitrittserklärung</div>
  <div class="field" style="left:504px;top:74px;width:195px">Name, Vorname</div>
  <div class="field" style="left:504px;top:99px;width:195px">für die Institution/Firma + persönlich</div>
  <div class="field" style="left:504px;top:124px;width:195px">Straße, Hausnr.</div>
  <div class="field" style="left:504px;top:149px;width:195px">PLZ, Ort</div>
  <div class="field" style="left:504px;top:174px;width:195px">Telefon/Handy</div>
  <div class="field" style="left:504px;top:199px;width:195px">Emailadresse</div>
  <div class="field" style="left:504px;top:224px;width:195px">Geburtstag</div>
  <div class="field" style="left:504px;top:262px;width:195px">Datum, Unterschrift</div>

  <div class="block" style="left:504px;top:328px;width:205px">
    <div class="heading" style="margin-bottom:10px">Mitgliedsbeiträge</div>
    <ul class="fees">
      <li>jeweils Mindestbeiträge</li>
      <li>Einzelpersonen 20 €</li>
      <li>Ehepaare/Partnerschaften 32€</li>
      <li>Institutionen/Firmen 95 €</li>
      <li><span class="blank"></span> €<small>Bitte frei wählbaren Betrag einfügen</small></li>
      <li>ich benötige eine Spendenbescheinigung</li>
      <li>Einmalige Spende (ohne Mitgliedschaft)</li>
    </ul>
  </div>
</section>

</body>
</html>
```